New Coffee Brand Packaging Design

We need a package design for our new coffee brand called Harkvale Coffee. Our brand mission will be displayed on the packaging (along the side or the back) and we currently have a logo that should be displayed on the front. Feel free to suggest a new logo design as you are designing the packaging if it doesn't fit with your vision. The final design should be creative and conservative. We like coffee colors (dark and light browns, white, cream, black, gold). We also like chalkboard art imagery (i.e. coffee cups, theme words from our mission, people, etc.). One famous person from West Louisville, KY is Cornelius Bray (world famous boxer and activist). If there is a way to draw his image in more of an abstract way where it doesn't infringe any patents that would be the sort of creativity we would like in the packaging. Our coffee brand prides itself on being a coffee for the people. For the average joe, working American who enjoys a good cup of coffee and a good atmosphere.

Harkvale Coffee Mission: "We aim to be a coffee company for the people. The people who have an appreciation and love for family, community and who never forget where they came from. Our coffee was born out of West Louisville, KY…a place like many others where the hearts, the minds and the wills are strong. We hope you enjoy each and every cup. Peace & Blessings."

Reason: Extending the deadline to see if there are more design ideas.

Requirements
Must have
• (On the side or on the back of the packaging) Harkvale Coffee Mission: "We aim to be a coffee company for the people. The people who have an appreciation and love for family, community and who never forget where they came from. Our coffee was born out of West Louisville, KY…a place like many others where the hearts, the minds and the wills are strong. We hope you enjoy each and every cup. Peace & Blessings."
Nice to have
• Coffee Colors: dark and light browns, white, cream, black, gold

```html
<!DOCTYPE html>
<html lang="en">
<head>
<meta charset="utf-8">
<title>Harkvale Coffee – Dark Roast Bag</title>
<link href="https://fonts.googleapis.com/css2?family=Tinos:wght@400;700&display=swap" rel="stylesheet">
<style>
  :root {
    --page: #ffffff;
    --bag: #0d0d0d;
    --bag-edge: #1a1a1a;
    --ink: #f4f1ea;
    --accent: #ee6a24;
    --art-yellow: #f6e98a;
    --art-orange: #e9962e;
    --art-plum: #7a1c3a;
  }
  * { margin: 0; padding: 0; box-sizing: border-box; }
  html, body { width: 1200px; height: 1200px; overflow: hidden; background: var(--page); }
  .canvas { position: relative; width: 1200px; height: 1200px; font-family: "Tinos", "Times New Roman", serif; color: var(--ink); }

  /* gusset (side panel) */
  .gusset { position: absolute; left: 0; top: 0; }
  .gusset-badge {
    position: absolute; left: 324px; top: 554px; width: 82px; height: 82px;
    border: 9px solid var(--accent); border-radius: 50%;
    display: flex; align-items: center; justify-content: center;
    font-size: 9px; font-weight: 400; color: var(--ink); text-align: center; line-height: 1.1;
  }
  .gusset-copy {
    position: absolute; left: 300px; top: 736px; width: 122px;
    font-size: 8.5px; line-height: 17.3px; text-align: center; color: var(--ink);
  }
  .gusset-copy span { display: block; white-space: nowrap; }

  /* front panel */
  .front {
    position: absolute; left: 443px; top: 213px; width: 303px; height: 710px;
    background: var(--bag);
    clip-path: polygon(0 0, 100% 0.3%, 99.6% 100%, 0.4% 99.8%);
  }
  .front-art {
    position: absolute; left: 5px; top: 102px; width: 297px; height: 325px;
    background:
      radial-gradient(ellipse at 30% 20%, var(--art-plum) 0 18%, transparent 38%),
      radial-gradient(ellipse at 85% 70%, var(--art-orange) 0 15%, transparent 35%),
      linear-gradient(160deg, transparent 0 35%, var(--art-orange) 50%, var(--art-yellow) 75%);
    clip-path: polygon(20% 0, 55% 0, 60% 30%, 100% 40%, 100% 100%, 0 100%, 0 55%, 30% 30%);
  }
  .brand-name {
    position: absolute; left: 0; right: 0; top: 460px; text-align: center;
    font-weight: 400; color: var(--ink); line-height: 1;
  }
  .brand-name .word { display: block; font-size: 62px; letter-spacing: 1px; }
  .brand-name .sub { display: block; font-size: 19px; letter-spacing: 4px; text-transform: uppercase; margin-top: 6px; padding-left: 120px; }
  .roast-row { position: absolute; left: 0; right: 0; top: 587px; height: 58px; }
  .roast-origin { position: absolute; left: 14px; top: 14px; font-size: 23px; font-weight: 700; }
  .roast-level { position: absolute; left: 184px; top: 12px; font-size: 27px; font-weight: 700; letter-spacing: 1px; }
  .roast-divider { position: absolute; left: 166px; top: 0; width: 5px; height: 58px; border-left: 1px solid var(--ink); border-right: 1px solid var(--ink); }
  .net-weight { position: absolute; left: 0; right: 0; top: 684px; text-align: center; font-size: 12.5px; font-weight: 700; }
</style>
</head>
<body>
<main class="canvas">
  <svg class="gusset" width="1200" height="1200" aria-hidden="true">
    <polygon points="325,213 389,213 424,925 300,925" fill="var(--bag)" stroke="var(--bag-edge)" stroke-width="1"/>
  </svg>
  <div class="gusset-badge">Harkvale<br>Coffee</div>
  <p class="gusset-copy">
    <span>Phasellus vel diam no</span>
    <span>n tellus rhoncus placerat.</span>
    <span>Proin id est lectus. Aliqu</span>
    <span>am dignissim molestie ar</span>
    <span>cu quis accumsan. Ut ma</span>
    <span>gna orci, venenatis rhoncus</span>
    <span>dolor nec, commodo pla</span>
  </p>

  <section class="front">
    <div class="front-art" role="img" aria-label="Watercolour illustration of plum and orange lily flowers on a green stem over a pale yellow wash"></div>
    <h1 class="brand-name"><span class="word">Harkvale</span><span class="sub">Coffee</span></h1>
    <div class="roast-row">
      <span class="roast-origin">100% Arabia</span>
      <span class="roast-divider"></span>
      <span class="roast-level">DARK</span>
    </div>
    <p class="net-weight">Net Weight 63oz (1 lb)) 453 g</p>
  </section>
</main>
</body>
</html>
```